Park furniture company needs a new product flyer

We're a street and park furniture supply company and we have a new range of furniture that we would like to showcase to prospective customers.
Pictures, logo and copy attached.
Furniture pictures are also available with a black background.
Warranty information needs to feature on the flyer.
Recycled content information needs to feature on the flyer.

Target Market(s)

Landscape Architects

Font styles to use
Serif

Requirements
Must have
• Professional fonts and graphics.
Should not have
• comic sans or similar fonts - cheap graphics

```html
<!DOCTYPE html>
<html lang="en">
<head>
<meta charset="utf-8">
<title>Kerbline Park Works – Product Flyer</title>
<link href="https://fonts.googleapis.com/css2?family=Montserrat:wght@300;400;700&family=Oswald:wght@500;600&family=Open+Sans:wght@400&display=swap" rel="stylesheet">
<style>
  :root {
    --page-bg: #e4e4e4;
    --paper: #ffffff;
    --paper-tint: #f1f2f4;
    --brand-blue: #1f78c1;
    --brand-red: #c01e25;
    --ink-dark: #4a4a4c;
    --ink-text: #2e2e30;
    --frame-grey: #b9b9bb;
    --timber: #9a4a1c;
    --timber-light: #c26a30;
    --alu: #b9a78a;
    --white: #ffffff;
  }
  * { box-sizing: border-box; margin: 0; padding: 0; }
  html, body { width: 1200px; height: 1083px; overflow: hidden; }
  body { background: var(--page-bg); position: relative; font-family: "Open Sans", sans-serif; }

  .flyer {
    position: absolute; left: 240px; top: 32px;
    width: 720px; height: 1018px;
    background: linear-gradient(160deg, var(--paper-tint) 0%, var(--paper) 45%, var(--paper-tint) 100%);
    overflow: hidden;
    box-shadow: 0 6px 24px rgba(0,0,0,0.18);
  }

  .brand {
    position: absolute; left: 110px; top: 92px;
    display: flex; align-items: center; gap: 14px;
    font-family: "Montserrat", sans-serif; font-weight: 700;
    font-size: 42px; letter-spacing: 1px; color: var(--ink-dark);
  }
  .brand-square { width: 22px; height: 22px; background: var(--brand-blue); }

  .hero-band {
    position: absolute; left: 0; top: 200px; width: 720px; height: 240px;
    background: var(--brand-blue);
  }
  .headline {
    position: absolute; left: 40px; top: 218px; width: 470px;
    font-family: "Montserrat", sans-serif; font-weight: 300;
    font-size: 28px; line-height: 1.22; color: var(--white);
  }
  .headline strong { font-weight: 700; }
  .headline .lead { font-size: 34px; }

  .warranty-band {
    position: absolute; left: 0; top: 440px; width: 515px; height: 96px;
    background: var(--brand-red);
  }
  .warranty-box {
    position: absolute; left: 40px; top: 452px; width: 460px; height: 72px;
    border: 1.5px solid var(--white);
    display: flex; align-items: center; justify-content: center;
    font-family: "Oswald", sans-serif; font-weight: 600;
    font-size: 50px; color: var(--white); letter-spacing: 0.5px;
  }

  .hero-product {
    position: absolute; left: 525px; top: 165px; width: 180px; height: 395px;
    background: linear-gradient(150deg, var(--timber-light) 0%, var(--timber) 55%, var(--alu) 100%);
    border-radius: 4px;
  }

  .gallery { position: absolute; left: 40px; top: 566px; }
  .gallery-frame {
    width: 200px; height: 104px; margin-bottom: 10px;
    border: 8px solid var(--frame-grey); background: var(--white);
    padding: 7px; box-shadow: 2px 4px 8px rgba(0,0,0,0.15);
  }
  .gallery-photo {
    width: 100%; height: 100%;
    background: linear-gradient(170deg, #ffffff 0%, #8a6a4f 55%, #d8cfc2 100%);
  }
  .gallery-frame:nth-child(2) .gallery-photo {
    background: linear-gradient(170deg, #ffffff 0%, var(--timber-light) 50%, #d8cfc2 100%);
  }

  .features {
    position: absolute; left: 282px; top: 580px; width: 405px;
    list-style: none; font-size: 12px; line-height: 1.42; color: var(--ink-text);
  }
  .features li { position: relative; padding-left: 20px; margin-bottom: 8px; }
  .features svg { position: absolute; left: 0; top: 2px; width: 12px; height: 12px; }

  .call-tab {
    position: absolute; right: 0; top: 912px; width: 470px; height: 56px;
    background: var(--ink-dark);
    clip-path: polygon(42px 0, 100% 0, 100% 100%, 0 100%);
    display: flex; align-items: center; justify-content: center; gap: 14px;
    font-family: "Oswald", sans-serif; font-weight: 600; font-size: 32px; color: var(--white);
  }
  .call-tab svg { width: 32px; height: 32px; }

  .info-bar {
    position: absolute; left: 0; top: 968px; width: 720px; height: 50px;
    background: var(--brand-blue);
    display: flex; align-items: center; justify-content: center; gap: 12px;
    font-family: "Oswald", sans-serif; font-weight: 500; font-size: 25px; color: var(--white);
  }
  .info-bar svg { width: 24px; height: 24px; }
</style>
</head>
<body>
  <main class="flyer">
    <div class="brand"><span class="brand-square"></span>Kerbline Park Works</div>

    <div class="hero-band"></div>
    <h1 class="headline">
      <span class="lead">European <strong>inspired</strong></span><br>
      with a <strong>unique</strong> and<br>
      <strong>original design</strong>, that is<br>
      functional all while respecting<br>
      <strong class="lead">the Environment.</strong>
    </h1>

    <div class="hero-product" role="img" aria-label="Photo of a park bench with timber-look composite battens and aluminium frame with armrests"></div>

    <div class="warranty-band"></div>
    <div class="warranty-box">10-YEAR WARRANTY</div>

    <div class="gallery">
      <div class="gallery-frame"><div class="gallery-photo" role="img" aria-label="Photo of a table with matching bench seat"></div></div>
      <div class="gallery-frame"><div class="gallery-photo" role="img" aria-label="Photo of a park seat with backrest and armrests"></div></div>
      <div class="gallery-frame"><div class="gallery-photo" role="img" aria-label="Photo of a picnic table setting with two benches"></div></div>
    </div>

    <ul class="features">
      <li><svg viewBox="0 0 14 14"><circle cx="7" cy="7" r="6" fill="none" stroke="#1f78c1" stroke-width="1.2"/><path d="M4 7.2l2 2 4-4" fill="none" stroke="#1f78c1" stroke-width="1.3"/></svg>Our range is designed to make life easier for people; created using extremely durable, ultra low maintenance materials.</li>
      <li><svg viewBox="0 0 14 14"><circle cx="7" cy="7" r="6" fill="none" stroke="#1f78c1" stroke-width="1.2"/><path d="M4 7.2l2 2 4-4" fill="none" stroke="#1f78c1" stroke-width="1.3"/></svg>Featuring 98% recycled composite battens in a range of stain and fade-resistant colour options and a unique aluminium frame design.</li>
      <li><svg viewBox="0 0 14 14"><circle cx="7" cy="7" r="6" fill="none" stroke="#1f78c1" stroke-width="1.2"/><path d="M4 7.2l2 2 4-4" fill="none" stroke="#1f78c1" stroke-width="1.3"/></svg>The capped composite battens come with a 10-year commercial warranty covering staining, fading and structural performance.</li>
      <li><svg viewBox="0 0 14 14"><circle cx="7" cy="7" r="6" fill="none" stroke="#1f78c1" stroke-width="1.2"/><path d="M4 7.2l2 2 4-4" fill="none" stroke="#1f78c1" stroke-width="1.3"/></svg>Site-specific for healthcare applications offering wheelchair accessibility options</li>
      <li><svg viewBox="0 0 14 14"><circle cx="7" cy="7" r="6" fill="none" stroke="#1f78c1" stroke-width="1.2"/><path d="M4 7.2l2 2 4-4" fill="none" stroke="#1f78c1" stroke-width="1.3"/></svg>The Kerbline Park Works range comprises of a seat with optional armrests, bench seat and table, available in both standard or DDA designs.</li>
      <li><svg viewBox="0 0 14 14"><circle cx="7" cy="7" r="6" fill="none" stroke="#1f78c1" stroke-width="1.2"/><path d="M4 7.2l2 2 4-4" fill="none" stroke="#1f78c1" stroke-width="1.3"/></svg>Uniform length of 1800mm with tailored options available.</li>
      <li><svg viewBox="0 0 14 14"><circle cx="7" cy="7" r="6" fill="none" stroke="#1f78c1" stroke-width="1.2"/><path d="M4 7.2l2 2 4-4" fill="none" stroke="#1f78c1" stroke-width="1.3"/></svg>Bolt down or freestanding options.</li>
    </ul>

    <div class="call-tab">
      <span>CALL US</span>
      <svg viewBox="0 0 32 32"><circle cx="16" cy="16" r="15" fill="#ffffff"/><circle cx="16" cy="16" r="12" fill="none" stroke="#1f78c1" stroke-width="2"/><path d="M12 9c1 0 2 3 2 4s-1.5 1.2-1.2 2.2c.6 1.6 1.8 2.9 3.3 3.6 1 .4 1.3-1.1 2.2-1.1s4 1.2 4 2.2c0 1.6-1.6 3-3 3-5 0-10-5-10-10 0-1.5 1.3-3.9 2.7-3.9z" fill="#1f78c1"/></svg>
      <span>0123 456 780</span>
    </div>

    <div class="info-bar">
      <span>FOR MORE INFORMATION VISIT</span>
      <svg viewBox="0 0 24 24" fill="none" stroke="#ffffff" stroke-width="1.6"><circle cx="12" cy="12" r="10"/><ellipse cx="12" cy="12" rx="4.5" ry="10"/><path d="M2 12h20M4 7h16M4 17h16"/></svg>
      <span>WWW.KERBLINEPARKWORKS.COM.AU</span>
    </div>
  </main>
</body>
</html>
```